20 year old business card needs re-design

We need to redesign our corporate business card look. We need something that appears more modern, eye catchy but professional.

Target Market(s)

manufacturing industry

Industry/Entity Type

Manufacturer

Contact Information for Business Card

One side can have the logo. Other side can have contact information.

Font styles to use
Serif

Colors
3277b5
33b8a4
ffffff

Requirements
Must have
• Eye catchy - need to standout from the crowd. company logo cannot change. Full name, job title, phone number and email address.
Should not have
• Fax, business address is not necessary.

```html
<!DOCTYPE html>
<html lang="en">
<head>
<meta charset="UTF-8">
<title>Norvel Works – Business Card</title>
<link href="https://fonts.googleapis.com/css2?family=Merriweather:wght@700&family=Roboto:wght@400;700&display=swap" rel="stylesheet">
<style>
  :root {
    --stage: #3a3a3c;
    --paper: #f4f4f4;
    --paper-shade: #e6e6e6;
    --brand-blue: #0c4ea6;
    --brand-blue-deep: #123f8c;
    --accent-teal: #33b8a4;
    --ink: #1d1d1d;
    --white: #ffffff;
  }
  * { box-sizing: border-box; margin: 0; padding: 0; }
  html, body { width: 1200px; height: 834px; overflow: hidden; }
  body {
    background: var(--stage);
    font-family: "Roboto", Arial, sans-serif;
    display: flex;
    align-items: center;
    justify-content: center;
    gap: 40px;
  }
  .card {
    position: relative;
    width: 540px;
    height: 309px;
    background: linear-gradient(135deg, var(--white), var(--paper) 60%, var(--paper-shade));
    overflow: hidden;
    box-shadow: 0 12px 30px rgba(0,0,0,.45);
  }
  .wordmark {
    position: absolute;
    left: 0; right: 0;
    display: flex;
    align-items: center;
    justify-content: center;
    gap: 12px;
    font-family: "Roboto", Arial, sans-serif;
    font-weight: 700;
    font-size: 40px;
    letter-spacing: -0.5px;
    color: var(--ink);
  }
  .wordmark-square {
    width: 26px; height: 26px;
    background: var(--brand-blue);
  }
  /* Front */
  .card--front .wordmark { top: 78px; }
  .tagline-band {
    position: absolute;
    left: 0; right: 0;
    top: 176px;
    height: 84px;
    background: var(--brand-blue);
    display: flex;
    align-items: center;
    justify-content: center;
    text-align: center;
    color: var(--white);
    font-size: 13px;
    line-height: 1.35;
  }
  /* Back */
  .card--back .wordmark { top: 62px; }
  .info-panel {
    position: absolute;
    left: 0; right: 0;
    top: 150px;
    height: 118px;
    background: linear-gradient(120deg, var(--brand-blue), var(--brand-blue-deep));
    border-top: 3px solid var(--accent-teal);
    border-bottom: 3px solid var(--accent-teal);
  }
  .info-pointer {
    position: absolute;
    left: 56px; top: 0;
    width: 0; height: 0;
    border-left: 9px solid transparent;
    border-right: 9px solid transparent;
    border-top: 9px solid var(--accent-teal);
  }
  .person {
    position: absolute;
    left: 38px;
    bottom: 22px;
  }
  .person-name {
    font-family: "Merriweather", Georgia, serif;
    font-weight: 700;
    font-size: 19px;
    color: var(--white);
  }
  .person-title {
    font-size: 14px;
    color: var(--accent-teal);
    margin-top: 3px;
  }
  .contact-list {
    position: absolute;
    right: 36px;
    top: 22px;
    list-style: none;
    color: var(--white);
    font-size: 12px;
  }
  .contact-list li {
    display: flex;
    align-items: center;
    gap: 8px;
    margin-bottom: 8px;
  }
  .contact-icon { width: 13px; height: 13px; flex: none; }
</style>
</head>
<body>
  <section class="card card--front" aria-label="Card front">
    <div class="wordmark"><span class="wordmark-square"></span>Norvel Works</div>
    <div class="tagline-band">
      <p>International Manufacturing Solutions for OEM<br>customers in North America</p>
    </div>
  </section>

  <section class="card card--back" aria-label="Card back">
    <div class="wordmark"><span class="wordmark-square"></span>Norvel Works</div>
    <div class="info-panel">
      <span class="info-pointer"></span>
      <ul class="contact-list">
        <li>
          <svg class="contact-icon" viewBox="0 0 16 16" fill="none" stroke="#33b8a4" stroke-width="1.5"><path d="M4 1.5l2.5 3-1.5 1.5c.8 1.8 2.2 3.2 4 4l1.5-1.5 3 2.5-1.5 2.5C6.5 13 3 9.5 1.5 4z"/></svg>
          555-014-2290 xt118
        </li>
        <li>
          <svg class="contact-icon" viewBox="0 0 16 16" fill="none" stroke="#33b8a4" stroke-width="1.5"><rect x="1.5" y="3.5" width="13" height="9"/><path d="M1.5 3.5l6.5 5 6.5-5"/></svg>
          dan@norvelworks.com
        </li>
        <li>
          <svg class="contact-icon" viewBox="0 0 16 16" fill="none" stroke="#33b8a4" stroke-width="1.5"><circle cx="8" cy="8" r="6.5"/><path d="M1.5 8h13M8 1.5c2.5 3 2.5 10 0 13M8 1.5c-2.5 3-2.5 10 0 13"/></svg>
          www.norvelworks.com
        </li>
      </ul>
      <div class="person">
        <p class="person-name">Dan Keller</p>
        <p class="person-title">President</p>
      </div>
    </div>
  </section>
</body>
</html>
```